Institutional website for an IT Consulting company

Web design + HTML + CSS / Bootstrap + JS (interaction) integration in order to extend our existing website brightvale.coop.
Our website is currently aiming only for recruitment and not for customers, we want to provide a fluid transition between customer side website (this project) and recruitment website (existing site).

Ideally we would love the new design to be "inspired" by our actual graphic chart (Colors mainly). It should provide a great user experience and a landing page (or any mean) allowing the visitor to easily switch from the end customer front end (this project), the recruitment front end (existing front end https://www.brightvale.coop/) and the existing member front end (an other existing front end dedicated to members already existing).

In attachment you will find the expected site content mainly a one page with a first level of information and "link" to sub pages (a way to directly access this sub pages should also be provided).

The website should be accessible on mobile device and desktop.

The attachment is in french as it reflect the final site content, but if google translate isn't sufficient to have a general idea of the content, feel free to ask. We would love to have some visual representation for some categories.

Target Market(s)

fortune 500 companies

Industry/Entity Type

It Company

Coding

Coded - Design and coding required

Number of Pages Required

5+ page

Requirements
Must have
• This project must have an easy way to navigate between 3 sub sites, the customer one (the one designed here), the consultant / recruitment one (the existing one at brightvale.coop), the members one.

A one page experience at first leading to detail pages.

Custom made visuals to illustrate each categories.

Inspiration websites : quorb[.]fr ; tasknest[.]com ; dovrally[.] com ...

Be inspired by the existing color from our logo and existing website at brightvale[.]coop

```html
<!DOCTYPE html>
<html lang="en">
<head>
<meta charset="utf-8">
<title>Brightvale.coop — Why use an AEC-COPA?</title>
<link href="https://fonts.googleapis.com/css2?family=Montserrat:ital,wght@0,500;0,600;0,700;1,400&family=Open+Sans:ital,wght@0,400;0,600;1,400&display=swap" rel="stylesheet">
<style>
:root{
  --teal:#16aab5;
  --teal-dark:#0f9aa5;
  --ink-green:#0f4a4c;
  --heading:#333333;
  --body:#5b5b5b;
  --muted:#8a8a8a;
  --line:#d8d8d8;
  --band:#f0f0f0;
  --white:#ffffff;
  --badge:#c9c9c9;
}
*{box-sizing:border-box;margin:0;padding:0}
html,body{width:1200px;height:4360px;overflow:hidden;background:var(--white)}
body{position:relative;font-family:"Open Sans",Arial,sans-serif;color:var(--body)}
.abs{position:absolute}
h1,h2,h3,h4{font-family:"Montserrat",Arial,sans-serif;color:var(--heading)}

/* header */
.site-header{left:0;top:0;width:1200px;height:122px;background:var(--white)}
.brand{font-family:"Montserrat",Arial,sans-serif;font-weight:700;color:var(--ink-green);letter-spacing:1px;display:flex;align-items:center;gap:12px}
.brand-square{width:18px;height:18px;background:var(--teal)}
.header-brand{left:110px;top:34px;font-size:38px}
.util-links{right:112px;top:16px;font-family:"Montserrat",sans-serif;font-size:14px;font-weight:600;color:#444;display:flex;gap:12px;align-items:center}
.util-links .ico{display:inline-block;width:12px;height:12px;border-radius:50%;background:var(--teal);margin-right:6px;vertical-align:-1px}
.nav{top:51px;left:532px;display:flex;gap:18px}
.nav a{display:block;height:48px;line-height:46px;padding:0 14px;border:2px solid #9a9a9a;font-family:"Montserrat",sans-serif;font-size:14px;font-weight:600;color:#555;text-decoration:none;white-space:nowrap}
.nav a.cta{background:#2a2a2a;border-color:#2a2a2a;color:var(--white)}

/* hero */
.hero{left:0;top:122px;width:1200px;height:403px;background:linear-gradient(90deg,#f4f4f4 0%,#ececec 40%,#d9d6d2 65%,#b9ada2 100%)}
.hero-photo{left:560px;top:0;width:640px;height:403px;background:radial-gradient(ellipse at 70% 55%,#c9a58c 0%,#9d8270 30%,rgba(210,205,200,0) 70%)}
.hero h1{left:112px;top:104px;font-weight:600;font-size:51px;line-height:1.2;color:#2d2d2d}
.hero h1 strong{display:block;font-weight:700;font-size:68px}
.dots{left:550px;top:344px;display:flex;gap:12px}
.dots span{width:18px;height:18px;border-radius:50%;border:2px solid #666}
.dots span.on{background:#666}

/* feature sections */
.circle{width:394px;height:394px;border-radius:50%;background:var(--white);box-shadow:0 6px 22px rgba(0,0,0,.12)}
.circle .visual{position:absolute;left:77px;top:77px;width:240px;height:240px;border-radius:50%;background:radial-gradient(circle,#d8f1f3 0%,#eef7f8 60%,#ffffff 100%)}
.feature h2{font-size:42px;font-weight:700;line-height:60px;text-transform:uppercase;color:#333}
.feature p{font-size:14px;line-height:27.5px;color:var(--body)}
.feature p + p{margin-top:27px}
.feature .lead{font-family:"Montserrat",sans-serif;font-weight:600;font-size:19px;line-height:31px;color:#333;margin-top:18px}
.feature h3{font-size:26px;font-weight:500;margin:16px 0 6px;color:#333}

/* partners */
.partners{left:0;top:3205px;width:1200px;height:279px;background:var(--band)}
.section-title{width:1200px;text-align:center;font-size:40px;font-weight:700;text-transform:uppercase}
.partners .section-title{top:66px;color:#222}
.badge{top:140px;width:181px;height:85px;border:5px solid var(--badge);background:var(--white);display:flex;align-items:center;justify-content:center}
.badge span{width:110px;height:24px;background:#e2e2e2;border-radius:3px}
.badge.active{border-color:var(--teal)}
.badge.active span{background:#2c2c2c;width:120px;height:20px}
.chev{font-family:"Montserrat",sans-serif;font-size:44px;color:#999;line-height:1}

/* testimonials */
.testimonials{left:0;top:3484px;width:1200px;height:464px;background:linear-gradient(135deg,#17b0bb 0%,#12a6b1 60%,#19b6c1 100%)}
.testimonials .section-title{top:50px;color:var(--white)}
.quote-card{top:129px;width:306px;height:261px;border:3px solid rgba(255,255,255,.55);color:var(--white);text-align:center;padding:30px 26px 0}
.quote-card.featured{background:var(--white);border-color:var(--white);color:#444}
.quote-card blockquote{font-style:italic;font-size:16px;line-height:27px}
.author{position:absolute;left:54px;top:156px;display:flex;align-items:center;gap:20px;text-align:left}
.avatar{width:96px;height:96px;border-radius:50%;background:radial-gradient(circle at 50% 40%,#d9c0a8,#8d745f);border:3px solid var(--white)}
.author b{display:block;font-family:"Montserrat",sans-serif;font-weight:500;font-size:19px}
.author small{font-family:"Montserrat",sans-serif;font-weight:600;font-size:14px}
.tchev{color:var(--white);font-size:44px;font-family:"Montserrat",sans-serif;top:3740px}

/* footer */
.footer-brand{left:110px;top:4084px;font-size:38px}
.fcol{top:4000px}
.fcol h4{font-size:19px;font-weight:600;margin-bottom:10px;color:#333}
.fcol li{list-style:none;font-size:14px;line-height:27px;color:#555}
.fcol .gap{margin-top:27px}
.pin{display:inline-block;width:10px;height:10px;border-radius:50% 50% 50% 0;transform:rotate(-45deg);background:var(--teal);margin-right:10px}
.footer-rule{left:110px;top:4278px;width:980px;height:1px;background:var(--line)}
.copyright{left:110px;top:4310px;font-size:14px;color:#555}
.social{top:4300px;width:42px;height:42px;border-radius:50%;border:2px solid #bbb;display:flex;align-items:center;justify-content:center}
.social span{width:10px;height:10px;border-radius:50%;background:var(--teal)}
</style>
</head>
<body>

<header class="site-header abs">
  <div class="brand header-brand abs">brightvale.coop<span class="brand-square"></span></div>
  <div class="util-links abs"><span><i class="ico"></i>LOG IN</span><span>|</span><span><i class="ico"></i>HELP</span></div>
  <nav class="nav abs">
    <a href="#">I AM BRIGHTVALE</a>
    <a href="#">I WISH TO JOIN BRIGHTVALE</a>
    <a href="#" class="cta">CONTACT US</a>
  </nav>
</header>

<section class="hero abs">
  <div class="hero-photo abs" role="img" aria-label="Smiling consultant in glasses working at a laptop"></div>
  <h1 class="abs">WHY USE A<strong>AEC–COPA?</strong></h1>
  <div class="dots abs"><span class="on"></span><span></span><span></span><span></span></div>
</section>

<!-- What is -->
<div class="circle abs" style="left:111px;top:604px"><div class="visual" role="img" aria-label="Icon of a laptop with a pencil"></div></div>
<article class="feature abs" style="left:570px;top:608px;width:520px">
  <h2>What is a AEC–COPA?</h2>
  <p style="margin-top:12px">Brightvale is an activity and employment cooperative which has the legal status of a cooperative and participatory association (SCOP in French). Do these words seem fuzzy to you? Here is an explanation that will allow you to understand how we operate:</p>
  <p>An AEC like Brightvale gathers a group of consultant who wish to develop their own entrepreneur activity whilst being part of a collective company and benefiting from the salaried status.<br>We chose the legal status of COPA so that each of our S/E can work on their professional activity whilst having the opportunity to profit from the contributors' experiences in their area. Because of this status, we adopted a democratic governance: all decision-making are taken by vote of the associated S/E. The S/E can become associated by simple request and have an obligation to become one after 3 years of service.</p>
  <p>Regarding the stewardship, it is a volunteer work that lasts for only 3 years and is available to all our S/E and has to be voted by all the S/E.</p>
</article>

<!-- Dual role -->
<article class="feature abs" style="left:110px;top:1204px;width:540px">
  <h2>A dual role:<br>entrepreneur and<br>salaried?</h2>
  <p style="margin-top:24px">Our consultant have a status of S/E in our COPA, a dual role that allows them to work directly with you in total autonomy whilst enjoying the benefits of being salaried: training account, paid vacation, health mutual etc.</p>
  <p>All our consultants have different profiles with different area of expertise that will meet your requirement in the data area.</p>
</article>
<div class="circle abs" style="left:696px;top:1188px"><div class="visual" role="img" aria-label="Icon of three people linked to a gear"></div></div>

<!-- Custom made -->
<div class="circle abs" style="left:109px;top:1628px"><div class="visual" role="img" aria-label="Icon of a hand choosing a document with a gear"></div></div>
<article class="feature abs" style="left:575px;top:1702px;width:520px">
  <h2>Custom–made?</h2>
  <p style="margin-top:12px">Our team is composed of different profiles who all have the same interest regarding data technologies with a specialization on Corvane tools. From junior to senior S/E, from development to advising and training or audit, we will be able to adapt to your needs.</p>
</article>

<!-- Collective -->
<article class="feature abs" style="left:108px;top:2076px;width:540px">
  <h2>A collective at<br>your service</h2>
  <p class="lead">Choosing a service delivery with Brightvale is working with a community, not a self-employed worker:</p>
  <h3>A support department at your disposal</h3>
  <p>A sales team is available to answer to all of your questions, whether their concern the way we operate our organisation or your research of service. Procedure simplified allowing agility in contracts.</p>
  <h3>Mutual help in our community</h3>
  <p>Mutual help is significant to us. It allows us to compare our ideas and to strengthen our skills to offer you the best possible service.</p>
  <h3>Shared technology watch</h3>
  <p>We keep up to date an internal tool where everyone can share the latest news on tools we use. We also set up meetings targeted at an expert or user audience about the use of technological tools or feedback on our experiences.</p>
</article>
<div class="circle abs" style="left:690px;top:2080px"><div class="visual" role="img" aria-label="Icon of a headset surrounded by arrows"></div></div>

<!-- Fair pay -->
<div class="circle abs" style="left:110px;top:2740px"><div class="visual" role="img" aria-label="Icon of a receipt with a dollar sign"></div></div>
<article class="feature abs" style="left:575px;top:2765px;width:520px">
  <h2>A fair pay</h2>
  <p style="margin-top:12px">Each invoice we make on behalf of Brightvale.coop is directly paid to the S/E. A fixed share is dedicated to the functioning of the commercial and administrative service. Nothing is simpler.</p>
  <p>Within Brightvale, everyone is responsible of its own wage according to its sales revenue. The S/E owns an analytical account he or she can manage and check at all times in order to track revenues and expenses throughout the year.</p>
</article>

<!-- Partners -->
<section class="partners abs">
  <h2 class="section-title abs">Featured partners</h2>
  <div class="chev abs" style="left:62px;top:158px">‹</div>
  <div class="badge abs" style="left:110px"><span></span></div>
  <div class="badge abs" style="left:309px"><span></span></div>
  <div class="badge active abs" style="left:508px"><span></span></div>
  <div class="badge abs" style="left:706px"><span></span></div>
  <div class="badge abs" style="left:905px"><span></span></div>
  <div class="chev abs" style="left:1102px;top:158px">›</div>
</section>

<!-- Testimonials -->
<section class="testimonials abs">
  <h2 class="section-title abs">Client testimonials</h2>
  <div class="quote-card abs" style="left:112px">
    <blockquote>“Nam libero tempore, cum soluta nobis est eligendi opticum que nihil impedit quo minus id quod maxime placeat facere possimus”</blockquote>
    <div class="author"><div class="avatar" role="img" aria-label="Client portrait"></div><div><b>John Doe</b><small>CEO</small></div></div>
  </div>
  <div class="quote-card featured abs" style="left:447px">
    <blockquote>“Nam libero tempore, cum soluta nobis est eligendi opticum que nihil impedit quo minus id quod maxime placeat facere possimus”</blockquote>
    <div class="author"><div class="avatar" role="img" aria-label="Client portrait"></div><div><b>John Doe</b><small>CEO</small></div></div>
  </div>
  <div class="quote-card abs" style="left:782px">
    <blockquote>“Nam libero tempore, cum soluta nobis est eligendi opticum que nihil impedit quo minus id quod maxime placeat facere possimus”</blockquote>
    <div class="author"><div class="avatar" role="img" aria-label="Client portrait"></div><div><b>John Doe</b><small>CEO</small></div></div>
  </div>
</section>
<div class="tchev abs" style="left:64px">‹</div>
<div class="tchev abs" style="left:1102px">›</div>

<!-- Footer -->
<div class="brand footer-brand abs">brightvale.coop<span class="brand-square"></span></div>
<div class="fcol abs" style="left:469px">
  <h4>Information</h4>
  <ul><li>About us</li><li>Team</li><li>Jobs</li><li>Hurry</li><li>Freelancing news</li><li>Data protection</li><li>Help</li><li>Sitemap</li></ul>
</div>
<div class="fcol abs" style="left:674px">
  <h4>Quick Links</h4>
  <ul><li>Offers and prices</li><li>Company</li><li>Open Brightvale coop</li><li>Insights</li><li>Create my Profile</li></ul>
</div>
<div class="fcol abs" style="left:880px">
  <h4>Find Us</h4>
  <ul>
    <li><i class="pin"></i>24 Rue des Tilleuls</li>
    <li style="padding-left:20px">75011 Paris</li>
    <li class="gap"><svg width="12" height="12" viewBox="0 0 12 12" style="margin-right:10px;vertical-align:-1px"><path d="M2 1h3l1 3-2 1a7 7 0 0 0 3 3l1-2 3 1v3c-6 1-10-3-9-9z" fill="#16aab5"/></svg>01 47 29 63 18</li>
    <li class="gap"><svg width="14" height="10" viewBox="0 0 14 10" style="margin-right:10px"><rect width="14" height="10" fill="#16aab5"/><path d="M0 0l7 5 7-5" stroke="#fff" fill="none"/></svg>contact@brightvale.coop</li>
  </ul>
</div>
<div class="footer-rule abs"></div>
<div class="copyright abs">© 2020, Brightvale.coop.</div>
<div class="social abs" style="left:946px"><span></span></div>
<div class="social abs" style="left:993px"><span></span></div>
<div class="social abs" style="left:1044px"><span></span></div>

</body>
</html>
```